Simple Wordpress "Coming soon" style website (1-3 sections) for a new games company.

This should be a relatively simple, but high-quality website, as it's only intended to be a placeholder for a later more complete website. 47K22P SEZC is a newly-established multi-platform games development company based in the Caribbean. We have a company logo. The logo is only three-colour and uses the Adobe Trajan font. Our business cards also use Adobe Georgia font for email/web addresses and phone numbers, as the Trajan font is capitals only. Our tagline is "Where Games Are Reimagined". Our first app, "Zorb", is in the final stages of development but it's not ready, so we need a "coming soon" style landing (splash) page, with "About Us", "Contact Us" and "Product Timeline" details. We have a Zorb product logo that can be included with the details, plus a screenshot of an in-progress game. The site design needs to allow for multilingual content. It doesn't require a translation plugin, as we've provided the "About Us" and "Product Timeline" content in 16 languages. The only contact details will be the email address. Examples of similar products / companies (if that helps) are "Dab The Tiles / Brinwell", "Jolly Shade / Q-Drift", and "Grid Sketch / CalmLoop". Please note that, with reference to the final selected design, we will need the ability to edit the content, as friends in all 15 countries will be supplying us with colloquially edited versions of the welcome blurb, and we can quickly supply replacement photographic imagery for any backgrounds or POS material. Please ask if you need any further information.
Target Market(s)
18-44yo puzzle gamers (40% male - 60% female)
Industry/Entity Type
Computer games industry
Coding
Coded - Design and coding required
Number of Pages Required
1 page
Font styles to use
Other font styles liked:
- See description
Look and feel

```html
<!DOCTYPE html>
<html lang="en">
<head>
<meta charset="utf-8">
<title>47K22P SEZC – Where Games Are Reimagined</title>
<link href="https://fonts.googleapis.com/css2?family=Cinzel:wght@700&family=Poppins:wght@400;500;600;700&display=swap" rel="stylesheet">
<style>
:root{
  --page:#0f1511;
  --footer:#0d100d;
  --white:#ffffff;
  --text:#e9eef0;
  --blue:#1f7fbf;
  --blue-dark:#1a6ea6;
  --green:#1c7a3c;
  --teal:#1d8a7e;
  --zorb:#2fc09a;
}
*{margin:0;padding:0;box-sizing:border-box}
html,body{width:895px;height:1200px;overflow:hidden;background:var(--page)}
body{position:relative;font-family:'Poppins',sans-serif;color:var(--text)}
.hero-bg{position:absolute;left:0;top:0;width:895px;height:530px;
  background:radial-gradient(ellipse at 70% 25%,rgba(150,150,70,.45),transparent 45%),
  radial-gradient(ellipse at 20% 40%,rgba(40,90,90,.5),transparent 55%),
  linear-gradient(180deg,#16241f 0%,#1b2e28 45%,#101812 100%)}
.timeline-bg{position:absolute;left:0;top:780px;width:895px;height:321px;
  background:radial-gradient(ellipse at 50% 95%,rgba(60,120,80,.55),transparent 55%),
  radial-gradient(ellipse at 20% 40%,rgba(50,60,120,.35),transparent 50%),
  linear-gradient(180deg,var(--page),#152318 70%,#1a2e22)}
.decor{position:absolute;left:0;top:520px;width:895px;height:280px}
.abs{position:absolute}
.brand{left:108px;top:34px;display:flex;align-items:center;gap:10px}
.brand-mark{width:44px;height:44px;border-radius:50%;background:var(--white)}
.brand-name{font-family:'Cinzel',serif;font-weight:700;font-size:24px;color:var(--white);letter-spacing:.5px}
.contact-top{left:578px;top:46px;display:flex;align-items:center;gap:8px;font-weight:600;font-size:10.5px;color:var(--white)}
.contact-top .mail-dot{width:23px;height:23px;border-radius:50%;background:var(--teal);display:flex;align-items:center;justify-content:center}
.lang{left:704px;top:47px;width:40px;height:22px;border:1px solid #ddd;padding:3px 4px;display:flex;align-items:center;gap:3px}
.lang .flag{width:19px;height:12px;background:#2a3f8f}
.lang .caret{width:0;height:0;border-left:3px solid transparent;border-right:3px solid transparent;border-top:4px solid #fff}
.menu{left:767px;top:49px;width:20px}
.menu span{display:block;height:3px;background:var(--white);border-radius:2px;margin-bottom:4px}
.product-name{left:0;width:895px;top:116px;text-align:center;font-weight:700;font-size:62px;color:var(--zorb);letter-spacing:2px}
.headline{left:0;width:895px;top:224px;text-align:center;font-family:'Cinzel',serif;font-weight:700;font-size:39px;line-height:43px;color:var(--white)}
.headline .accent{display:block;color:var(--blue)}
.about{left:172px;top:340px;width:552px;font-size:11px;line-height:16.7px;text-align:justify;text-align-last:center;color:var(--text)}
.about p+p{margin-top:19px}
.contact-line{left:0;width:895px;top:488px;text-align:center;font-size:17.5px;color:var(--white)}
.contact-line a{color:var(--white)}
.screenshot{left:252px;top:573px;width:368px;height:186px;border-radius:18px;
  background:linear-gradient(135deg,#5a3fb0,#8f9ad8 40%,#c9b8e6 60%,#4c3598)}
.timeline-title{left:0;width:895px;top:826px;display:flex;justify-content:center;align-items:center;gap:10px;font-family:'Cinzel',serif;font-weight:700;font-size:38px;color:var(--white)}
.timeline-title .mark{width:48px;height:48px;border-radius:50%;background:var(--blue-dark)}
.timeline-title .accent{color:var(--blue)}
.track{left:110px;top:973px;width:675px;height:3px;display:flex}
.track span{flex:1;background:var(--blue)}
.track span:nth-child(even){background:var(--green)}
.node{width:51px;height:51px;border-radius:50%;display:flex;align-items:center;justify-content:center;font-weight:600;font-size:10px;color:var(--white);transform:translateX(-50%)}
.node.up{top:914px;background:var(--blue)}
.node.down{top:984px;background:var(--green)}
.label{width:110px;transform:translateX(-50%);text-align:center;font-size:9.6px;line-height:13.5px;color:var(--text)}
.label.up{top:941px}
.label.up.two{top:928px}
.label.down{top:995px}
.footer{left:0;top:1101px;width:895px;height:99px;background:var(--footer)}
.copyright{left:108px;top:1143px;font-size:11.4px;color:var(--white)}
.social{top:1138px;width:31px;height:31px;border-radius:50%;background:var(--white)}
</style>
</head>
<body>
<div class="hero-bg" role="img" aria-label="Enchanted forest scene background in deep green and golden light"></div>
<svg class="decor" viewBox="0 0 895 280" aria-hidden="true">
  <circle cx="305" cy="95" r="72" fill="#173a45" opacity=".75"/>
  <circle cx="590" cy="195" r="72" fill="#173a26" opacity=".7"/>
  <circle cx="-10" cy="158" r="92" fill="none" stroke="#1c4a5e" stroke-width="22" opacity=".8"/>
  <circle cx="900" cy="170" r="100" fill="none" stroke="#1a4a2a" stroke-width="22" opacity=".8"/>
</svg>
<div class="timeline-bg" role="img" aria-label="Soft aurora landscape background in green and violet"></div>

<div class="abs brand"><span class="brand-mark"></span><span class="brand-name">47K22P SEZC</span></div>
<div class="abs contact-top">
  <span class="mail-dot"><svg width="10" height="8" viewBox="0 0 10 8"><rect x=".5" y=".5" width="9" height="7" rx="1" fill="#fff"/><path d="M.8 1 5 4.3 9.2 1" stroke="#1d8a7e" fill="none"/></svg></span>
  info@47k22p.ky
</div>
<div class="abs lang"><span class="flag"></span><span class="caret"></span></div>
<div class="abs menu"><span></span><span></span><span></span></div>

<div class="abs product-name">Zorb</div>
<h1 class="abs headline">47K22P SEZC - WHERE<span class="accent">GAMES ARE REIMAGINED</span></h1>
<div class="abs about">
  <p>Get ready to embark on an exhilarating journey with 47K22P SEZC, a dynamic, multi-platform game development company born in the heart of the Caribbean! Our diverse team hails from around the world, blending talent with passion. From fresh graduates to industry veterans, we've united under one vision: to radically reimagine existing games.</p>
  <p>With our debut title "Zorb," a captivating Colouring-In/PBN game for Nimbo, Kestra, Orvane, and PC, we're set to showcase what true innovation looks like. Stay tuned to see how we're reshaping the gaming landscape, one Pixel at a time!</p>
</div>
<p class="abs contact-line">Contact us by emailing <a href="mailto:info@47k22p.ky">info@47k22p.ky</a></p>

<div class="abs screenshot" role="img" aria-label="Screenshot of the Zorb colouring game running on a phone"></div>

<h2 class="abs timeline-title"><span class="mark"></span><span><span class="accent">ZORB</span> TIMELINE</span></h2>

<div class="abs track"><span></span><span></span><span></span><span></span><span></span><span></span><span></span></div>
<div class="abs node up" style="left:159px">Q3-23</div>
<div class="abs node up" style="left:354px">Q1-24</div>
<div class="abs node up" style="left:546px">Q3-24</div>
<div class="abs node up" style="left:736px">Q1-25</div>
<div class="abs node down" style="left:255px">Q4-23</div>
<div class="abs node down" style="left:450px">Q2-24</div>
<div class="abs node down" style="left:642px">Q3-24</div>
<div class="abs label up" style="left:254px">Proof of concept</div>
<div class="abs label up two" style="left:449px">Team gathering &amp;<br>pitch</div>
<div class="abs label up" style="left:643px">Zorb completed</div>
<div class="abs label down" style="left:155px">Zorb conceived</div>
<div class="abs label down" style="left:350px">Working game<br>(PC only)</div>
<div class="abs label down" style="left:547px">47K22P<br>established</div>
<div class="abs label down" style="left:737px">Zorb launched!</div>

<footer class="abs footer"></footer>
<p class="abs copyright">© 2024 Companyname. All rights reserved.Privacy &nbsp;|&nbsp; Terms of Use</p>
<span class="abs social" style="left:676px" aria-label="Social link"></span>
<span class="abs social" style="left:716px" aria-label="Social link"></span>
<span class="abs social" style="left:755px" aria-label="Social link"></span>
</body>
</html>
```